Quiet Harbor Hours Podcast Artwork

I need a cover for my podcast Quiet Harbor Hours that is clean, modern, and minimalist, but not too feminine

Target Market(s)

People struggling with fertility particularly women who are between the ages of 35-45 though there is a small set of listeners who are men

Requirements
Must have
• Embryo in the Zero
Should not have
• No script text

```html
<!DOCTYPE html>
<html lang="en">
<head>
<meta charset="utf-8">
<title>Quiet Harbor Hours – Podcast Cover</title>
<link rel="stylesheet" href="https://fonts.googleapis.com/css2?family=Open+Sans:ital,wght@0,300;1,800&display=swap">
<style>
  :root {
    --plum: #3b333f;
    --blush: #f7e4dc;
    --taupe: #9a8a88;
    --taupe-soft: #6f6369;
  }
  html, body {
    margin: 0;
    padding: 0;
    width: 1200px;
    height: 1200px;
    overflow: hidden;
    background: var(--plum);
  }
  .cover {
    position: relative;
    width: 1200px;
    height: 1200px;
    background: var(--plum);
    overflow: hidden;
  }
  .pattern-band {
    position: absolute;
    top: 0;
    height: 632px;
    width: 340px;
  }
  .pattern-band--left {
    left: 0;
    background: linear-gradient(90deg, var(--taupe-soft) 0%, rgba(111, 99, 105, 0.35) 100%);
  }
  .pattern-band--right {
    right: 0;
    background: linear-gradient(270deg, var(--taupe-soft) 0%, rgba(111, 99, 105, 0.35) 100%);
  }
  .emblem {
    position: absolute;
    left: 312px;
    top: 0;
    width: 576px;
    height: 576px;
  }
  .title {
    position: absolute;
    left: 0;
    right: 0;
    top: 640px;
    text-align: center;
    color: var(--blush);
    font-family: "Open Sans", Verdana, sans-serif;
  }
  .title__main {
    display: block;
    font-style: italic;
    font-weight: 800;
    font-size: 122px;
    line-height: 1;
    letter-spacing: -1px;
    margin-top: 60px;
  }
  .title__sub {
    display: block;
    font-weight: 300;
    font-size: 150px;
    line-height: 1;
    letter-spacing: 14px;
    margin-top: 54px;
  }
</style>
</head>
<body>
  <main class="cover">
    <div class="pattern-band pattern-band--left" role="img" aria-label="Decorative pattern of swimming sperm cells in muted taupe"></div>
    <div class="pattern-band pattern-band--right" role="img" aria-label="Decorative pattern of swimming sperm cells in muted taupe"></div>

    <svg class="emblem" viewBox="0 0 576 576" aria-hidden="false">
      <defs>
        <radialGradient id="embryo-tone" cx="55%" cy="50%" r="55%">
          <stop offset="0%" stop-color="#3b333f"/>
          <stop offset="100%" stop-color="#4a4150"/>
        </radialGradient>
      </defs>
      <circle cx="288" cy="288" r="282" fill="#f7e4dc" stroke="#9a8a88" stroke-width="12"/>
      <ellipse cx="300" cy="300" rx="180" ry="210" fill="url(#embryo-tone)" role="img" aria-label="Silhouette of a curled embryo with umbilical cord"/>
    </svg>

    <h1 class="title">
      <span class="title__main">QUIET HARBOR</span>
      <span class="title__sub">HOURS</span>
    </h1>
  </main>
</body>
</html>
```